Full Page 40k PSI Water Blasting / Water Jetting Ad

We need a full page ad showing our logo and maybe a few parts we supply. Ad background possibly showing the industries we cater to via picture rather it's a picture of a shipyard, airport runway, industrial plant or oil rig or all four.
- Somewhere on the ad state the following..."Providing Economical Alternatives To The UHP Mobile Water Blasting Industry."
- Maybe add somewhere stating...."When The Pressure&'s Choose BRV."

What has to be on the ad.
- Leading Supplier of Dorwell Stamfry Quelbor Veratube Hose
- Numerous Styles of Sapphire Nozzles
- Wide Variety of Pump and Accessory Replacement Parts
- Brimvale Flow's Own Interchangeable Rotating Spurwand
- Fittings & Adapters
- Safety Gear

Target Market(s)

Contractors, Airport Runway Rubber Removal. Shipyard Waterblasting.

Requirements
Must have
• - Somewhere on the ad state the following..."Providing Economical Alternatives To The UHP Mobile Water Blasting Industry."
• - Maybe add somewhere stating.... "When The Pressure's Choose BRV."
• What has to be on the ad.
• - Leading Supplier of Dorwell Stamfry Quelbor Veratube Hose
• - Numerous Styles of Sapphire Nozzles
• - Wide Variety of Pump and Accessory Replacement Parts
• - Brimvale Flow's Own Interchangeable Rotating Spurwand
• - Fittings & Adapters
• - Safety Gear
Nice to have
• background possibly showing the industries we cater to via picture rather it's a picture of a shipyard, airport runway, industrial plant or oil rig or all four.
• Use a picture of our nozzles off our website.
• www.brimvaleflow.example

```html
<!DOCTYPE html>
<html lang="en">
<head>
<meta charset="utf-8">
<title>Brimvale Flow Technologies – Full Page Ad</title>
<link href="https://fonts.googleapis.com/css2?family=Oswald:wght@700&family=Roboto:wght@400;500&family=Libre+Baskerville:wght@700&display=swap" rel="stylesheet">
<style>
  :root{
    --page:#5aaad6;
    --paper:#eef0f4;
    --navy:#1c1a5e;
    --deep-blue:#1b2a7c;
    --mid-blue:#1a6fb6;
    --sky:#5bb8e6;
    --headline-blue:#1f6fb5;
    --yellow:#f3e62c;
    --ink:#1e1e24;
    --stamp:#c0262c;
  }
  *{margin:0;padding:0;box-sizing:border-box}
  html,body{width:1200px;height:810px;overflow:hidden;background:var(--page)}
  .ad{
    position:absolute;left:324px;top:10px;width:745px;height:1065px;
    transform:scale(0.7418);transform-origin:0 0;
    background:var(--paper);overflow:hidden;
    font-family:"Roboto",Arial,sans-serif;
  }
  .ad > *{position:absolute}
  .backdrop{left:0;top:0;width:745px;height:1065px}
  .brand{left:16px;top:30px;width:206px;text-align:center;color:var(--navy)}
  .brand-name{font-family:"Oswald",sans-serif;font-weight:700;font-size:58px;line-height:68px;color:var(--deep-blue);letter-spacing:2px}
  .brand-full{font-family:"Libre Baskerville",serif;font-weight:700;font-size:9.5px;margin-top:22px;white-space:nowrap}
  .brand-phone{font-size:22px;font-weight:500;margin-top:4px}
  .headline{left:28px;top:378px;font-family:"Oswald",sans-serif;font-weight:700;font-size:58px;line-height:73px;text-transform:uppercase;letter-spacing:.5px}
  .headline span{display:block}
  .blue{color:var(--headline-blue)}
  .navy{color:var(--navy)}
  .tagline{left:32px;top:672px;font-family:"Oswald",sans-serif;font-weight:700;font-size:42px;line-height:54px;text-transform:uppercase}
  .tagline span{display:block}
  .photo{border-radius:6px}
  .hose{left:492px;top:446px;width:240px;height:80px;border-radius:40px;background:linear-gradient(180deg,#f39a3c,#e0641a)}
  .gun{left:540px;top:603px;width:185px;height:104px;background:linear-gradient(135deg,#d9dbde,#8f9398);border-radius:14px}
  .nozzles{left:45px;top:838px;width:200px;height:68px;background:linear-gradient(180deg,#b9bcc0,#6e7277);border-radius:10px}
  .features{left:308px;top:690px;list-style:none;font-size:16.5px;line-height:21.4px;color:var(--ink)}
  .features li{padding-left:20px;position:relative}
  .features svg{position:absolute;left:0;top:7px;width:10px;height:9px}
  .contact{left:18px;top:920px;width:410px;height:130px;background:var(--navy);border-radius:30px;overflow:hidden}
  .partner{position:absolute;left:0;top:25px;width:157px;height:60px;background:#fff;display:flex;align-items:center;justify-content:center;font-family:"Oswald",sans-serif;font-weight:700;font-size:34px;color:var(--navy)}
  .follow{position:absolute;left:25px;top:96px;font-size:15px;color:#fff;display:flex;align-items:center;gap:6px}
  .follow i{display:inline-block;width:14px;height:14px;border-radius:50%;background:#fff}
  .follow i:first-of-type{margin-left:8px}
  .contact-title{position:absolute;left:180px;top:12px;font-family:"Oswald",sans-serif;font-weight:700;font-size:36px;color:var(--yellow);letter-spacing:.5px}
  .contact-list{position:absolute;left:183px;top:62px;list-style:none;color:#fff;font-size:14px;line-height:20px;letter-spacing:.2px}
  .contact-list li{display:flex;align-items:center;white-space:nowrap}
  .contact-list svg{width:14px;height:14px;margin-right:16px;flex:none}
</style>
</head>
<body>
<div class="ad">
  <svg class="backdrop" viewBox="0 0 745 1065">
    <defs>
      <linearGradient id="plant" x1="0" y1="0" x2="0" y2="1">
        <stop offset="0" stop-color="#55585c"/>
        <stop offset=".55" stop-color="#3a3d3f"/>
        <stop offset="1" stop-color="#1d1f22"/>
      </linearGradient>
      <linearGradient id="runway" x1="0" y1="0" x2="0" y2="1">
        <stop offset="0" stop-color="#4a3e3a"/>
        <stop offset="1" stop-color="#6b4a2e"/>
      </linearGradient>
    </defs>
    <path role="img" aria-label="Photo of an industrial power plant at night reflected in water" fill="url(#plant)"
      d="M250 0 H745 V262 C690 300 600 340 430 345 C305 340 240 270 232 170 C228 90 238 30 250 0 Z"/>
    <path fill="var(--sky)" d="M0 200 C120 230 240 300 400 345 C560 365 680 300 745 262 V280 C640 340 520 365 400 352 C240 330 120 300 0 280 Z"/>
    <path fill="var(--mid-blue)" d="M0 240 C140 290 260 320 400 345 C560 358 680 290 745 262 V290 C640 345 520 372 400 365 C240 358 120 340 0 330 Z"/>
    <path fill="var(--deep-blue)" d="M0 175 C110 210 220 290 330 340 C250 330 110 290 0 255 Z"/>
    <path fill="var(--sky)" d="M400 1065 C470 930 600 850 745 825 V845 C620 870 500 950 440 1065 Z"/>
    <path fill="var(--mid-blue)" d="M380 1065 C430 960 560 870 745 825 V835 C590 860 470 950 415 1065 Z"/>
    <path role="img" aria-label="Photo of an aircraft on an airport runway at dusk" fill="url(#runway)"
      d="M440 1065 C500 950 620 870 745 845 V1065 Z"/>
    <circle cx="662" cy="903" r="62" fill="none" stroke="var(--stamp)" stroke-width="4" opacity=".75"/>
    <circle cx="662" cy="903" r="48" fill="none" stroke="var(--stamp)" stroke-width="2" opacity=".75"/>
  </svg>

  <div class="brand">
    <div class="brand-name">BRV</div>
    <div class="brand-full">Brimvale Flow Technologies, Inc.</div>
    <div class="brand-phone">555 014 7720</div>
  </div>

  <h1 class="headline">
    <span class="blue">Providing Economical</span>
    <span class="blue">Alternatives To</span>
    <span class="navy">The UHP Mobile Water</span>
    <span class="navy">Blasting Industry</span>
  </h1>

  <div class="photo hose" role="img" aria-label="Coiled orange high-pressure hose with steel fitting"></div>
  <div class="photo gun" role="img" aria-label="Water blasting gun with orange grip"></div>

  <p class="tagline">
    <span class="navy">When The</span>
    <span class="navy">Pressure's</span>
    <span class="blue">Choose BRV</span>
  </p>

  <div class="photo nozzles" role="img" aria-label="Row of steel sapphire nozzles"></div>

  <ul class="features">
    <li><svg viewBox="0 0 10 9"><path d="M1 5 L4 8 L9 1" fill="none" stroke="#333" stroke-width="1.8"/></svg>Leading Supplier of Dorwell Stamfry<br>Quelbor Veratube Hose</li>
    <li><svg viewBox="0 0 10 9"><path d="M1 5 L4 8 L9 1" fill="none" stroke="#333" stroke-width="1.8"/></svg>Numerous Styles of Sapphire Nozzles</li>
    <li><svg viewBox="0 0 10 9"><path d="M1 5 L4 8 L9 1" fill="none" stroke="#333" stroke-width="1.8"/></svg>Wide Variety of Pump and<br>Accessory Replacement Parts</li>
    <li><svg viewBox="0 0 10 9"><path d="M1 5 L4 8 L9 1" fill="none" stroke="#333" stroke-width="1.8"/></svg>Brimvale Flow's Own Interchangeable<br>Rotating Spurwand</li>
    <li><svg viewBox="0 0 10 9"><path d="M1 5 L4 8 L9 1" fill="none" stroke="#333" stroke-width="1.8"/></svg>Fittings &amp; Adapters</li>
    <li><svg viewBox="0 0 10 9"><path d="M1 5 L4 8 L9 1" fill="none" stroke="#333" stroke-width="1.8"/></svg>Safety Gear</li>
  </ul>

  <div class="contact">
    <div class="partner">Dorwell</div>
    <div class="follow">follow us: <i></i><i></i></div>
    <div class="contact-title">CONTACT US:</div>
    <ul class="contact-list">
      <li><svg viewBox="0 0 14 14"><rect x="1" y="3" width="12" height="8" fill="none" stroke="#fff" stroke-width="1.3"/><path d="M1 3 L7 8 L13 3" fill="none" stroke="#fff" stroke-width="1.3"/></svg>info@brimvaleflow.example</li>
      <li><svg viewBox="0 0 14 14"><path d="M3 1 h3 l1 3 -2 1.5 c1 2 2 3 3.5 3.5 L10 7 l3 1 v3 c-6 1 -11 -4 -10 -10z" fill="#fff"/></svg>555-014-7720</li>
      <li><svg viewBox="0 0 14 14"><circle cx="7" cy="7" r="6" fill="none" stroke="#fff" stroke-width="1.2"/><ellipse cx="7" cy="7" rx="2.6" ry="6" fill="none" stroke="#fff" stroke-width="1.1"/><path d="M1 7 H13 M2 4 H12 M2 10 H12" stroke="#fff" stroke-width="1"/></svg>www.brimvaleflow.example</li>
    </ul>
  </div>
</div>
</body>
</html>
```